WP website design (Brantow)

We need a wordpress design for an established auction and real estate company based in Kentucky. The winning design will incorporate a professional color scheme with company logo in a clean layout with specified widgets. The design needs to consider that this will be developed on a responsive theme. Colors will complement the colors in the logo.

Industry/Entity Type

Real Estate

Font styles to use
Sans Serif

Requirements
Must have
• - Navigation:
1) Home 2) Auctions 3) Real Estate Listings 4) Our Services 5) Why Auctions 6) About Us 7) Past Auctions 8) Contact Us

Homeage will have slideshow, please use stock real estate image as the initial slide. Homepage will have this content: "Martin Brantow Auctioneer Real Estate Broker

Buying or selling you can count on Martin Brantow Auctioneer to deliver a quality auction experience. We handle all the details from initial handshake to final payment. We are with you every step of the way giving our sellers the service and results they deserve. You only have one chance for a successful auction. Contact us today to see how our experience and know-how can work for you. We are confident that you will appreciate our higher standard of service."

Footer will have smaller company logo, and attached association logos and this contact info:
Phone: (270) 555-0148
Contacts: Martin Brantow
Email: martinbrantow@mailvex.example
Address: 482 Wexcombe Lane • Bowling Green, KY 42190

Widgets:
1) email sign up 2) Social media (twitter, Youtube - can also be in header 3) News & Events Blog widget 4) testimonials blog 5) Featured Video widget
Nice to have
• Nice to Have:
- demonstrate the drop-down menu styling, e.g. under Auctions
-Upcoming Auctions
-Online Auctions
-Past Auctions

```html
<!DOCTYPE html>
<html lang="en">
<head>
<meta charset="utf-8">
<title>Martin Brantow Auctioneer Real Estate Broker</title>
<link rel="stylesheet" href="https://fonts.googleapis.com/css2?family=Arimo:wght@400;700&family=Signika:wght@400;600&display=swap">
<style>
:root{
  --yellow:#f7c20b;
  --blue:#1b5cb0;
  --blue-dark:#0f4fa6;
  --blue-text:#1a5cab;
  --white:#ffffff;
  --page:#f2f2f2;
  --panel:#efefef;
  --border:#d8d8d8;
  --text:#444;
  --dark:#1e1e1e;
  --darker:#121212;
  --social-a:#2aa9e0;
  --social-b:#e0312c;
}
*{box-sizing:border-box;margin:0;padding:0}
html,body{width:1067px;height:1200px;overflow:hidden}
body{position:relative;background:var(--page);font-family:"Arimo",Arial,sans-serif;color:var(--text);font-size:11px}
.abs{position:absolute}
.top-band{left:0;top:0;width:1067px;height:460px;background:var(--yellow)}
.header{left:100px;top:13px;width:865px;height:114px;background:var(--white)}
.brand{left:26px;top:30px;display:flex;align-items:center;gap:8px}
.brand-mark{width:20px;height:20px;background:var(--blue)}
.brand-name{font-family:"Signika",sans-serif;font-weight:600;font-size:24px;color:var(--blue)}
.social{right:33px;top:53px;display:flex;align-items:center;gap:7px;font-size:19px;color:#555}
.social .label{margin-right:6px}
.social-box{width:26px;height:26px;border-radius:5px}
.social-box.first{background:var(--social-a)}
.social-box.second{background:var(--social-b)}
.nav{left:100px;top:134px;width:865px;height:41px;background:var(--blue);display:flex}
.nav a{display:flex;align-items:center;justify-content:center;white-space:nowrap;color:var(--white);text-decoration:none;font-size:13.5px;border-right:1px solid #3f7bc6;height:100%;flex:none}
.nav a:last-child{border-right:none;flex:1}
.dropdown{left:277px;top:176px;width:149px;background:var(--blue)}
.dropdown a{display:block;height:25px;line-height:25px;padding-left:19px;font-family:"Signika",sans-serif;font-size:11px;color:var(--white);text-decoration:none;border-bottom:1px solid #6d9bd6;white-space:nowrap}
.dropdown a.current{background:var(--yellow);color:#222}
.hero-frame{left:100px;top:184px;width:602px;height:258px;background:var(--white)}
.hero-photo{left:4px;top:4px;width:595px;height:250px;background:linear-gradient(180deg,#cfe3f4 0%,#e4e2dc 45%,#a79f93 75%,#d8d8d4 100%)}
.signup{left:702px;top:186px;width:263px;height:256px;background:var(--blue);color:var(--white)}
.signup h2{position:absolute;left:28px;top:16px;font-family:"Signika",sans-serif;font-weight:600;font-size:20px}
.signup label{position:absolute;left:30px;font-size:12.5px}
.signup .field{position:absolute;left:30px;width:204px;height:31px;background:var(--white)}
.signup .btn{position:absolute;left:143px;top:205px;width:87px;height:30px;background:var(--yellow);border-radius:3px;color:#222;font-family:"Signika",sans-serif;font-size:15px;display:flex;align-items:center;justify-content:center}
.content-bg{left:100px;top:460px;width:865px;height:607px;background:var(--white)}
.video{left:116px;top:482px;width:231px;height:155px;background:linear-gradient(180deg,#b8d2ea 0%,#c8d4c6 50%,#6f9a47 100%)}
.video-bar{left:116px;top:616px;width:231px;height:21px;background:#1d1d1d}
.video-bar .track{position:absolute;left:24px;top:9px;width:156px;height:3px;background:#777}
.video-bar .fill{position:absolute;left:24px;top:9px;width:80px;height:3px;background:#3b7ad0}
.play{left:217px;top:540px;width:42px;height:42px;border-radius:50%;background:rgba(40,40,40,.6);border:3px solid #ddd}
.widget{left:116px;width:231px;background:var(--panel);border:1px solid var(--border);border-radius:0 0 5px 5px}
.widget-head{height:33px;background:var(--blue-dark);color:var(--white);font-family:"Signika",sans-serif;font-size:16px;line-height:35px;padding-left:10px}
.testimonial{top:645px;height:182px}
.quote{font-size:11px;line-height:16px;color:#333;padding:0 8px 0 10px;text-indent:25px;margin-top:26px}
.qmark{font-family:Georgia,serif;font-size:22px;color:#bbb;position:absolute}
.author{position:absolute;left:10px;top:153px;font-weight:700;font-size:11px;color:#333}
.more{position:absolute;font-style:italic;color:var(--blue-text);font-size:11px}
.news{top:838px;height:181px}
.news ul{list-style:none;margin-top:26px;padding-left:12px;padding-right:20px;color:#333;line-height:18px}
.news li{position:relative;padding-left:10px;margin-bottom:16px}
.news li::before{content:"";position:absolute;left:0;top:6px;border-left:4px solid #444;border-top:3px solid transparent;border-bottom:3px solid transparent}
.main-title{left:382px;top:487px;font-family:"Signika",sans-serif;font-weight:400;font-size:18px;color:var(--blue-text);white-space:nowrap}
.intro{left:383px;top:521px;width:530px;line-height:17.8px;color:#555;font-size:10.8px}
.intro p{margin-bottom:17.8px}
.intro p.tight{margin-bottom:0}
.intro strong.name{color:var(--blue-text)}
.upcoming{left:382px;top:666px;font-family:"Signika",sans-serif;font-weight:400;font-size:17px;color:var(--blue-text)}
.auction{left:382px;top:702px;width:532px;height:288px;background:var(--panel);border:1px solid var(--border);border-radius:0 0 5px 5px}
.auction-head{height:36px;background:var(--blue-dark);color:var(--white);font-family:"Signika",sans-serif;font-weight:600;font-size:16px;line-height:38px;padding-left:11px;letter-spacing:.3px}
.box{position:absolute;background:var(--white);border:1px solid var(--border);border-radius:4px}
.thumb-box{left:7px;top:46px;width:101px;height:81px}
.thumb{position:absolute;left:6px;top:7px;width:88px;height:66px;background:linear-gradient(180deg,#d7e6f3,#c9bfb0 60%,#6f9348)}
.sale-tag{position:absolute;left:57px;top:26px;width:34px;height:32px;background:#d8262a}
.links-box{left:7px;top:134px;width:101px;height:90px}
.links-head{margin:4px;height:28px;background:var(--blue-dark);color:var(--white);font-family:"Signika",sans-serif;font-size:16px;line-height:30px;padding-left:8px}
.link{display:flex;align-items:center;gap:7px;padding-left:10px;font-weight:700;font-size:12px;color:#333;height:26px}
.info1{left:115px;top:46px;width:409px;height:98px;padding:8px 7px;font-size:11.5px;line-height:16px;color:#222}
.info1 .hl{color:var(--blue-text);font-weight:700}
.info2{left:115px;top:151px;width:409px;height:128px;padding:10px 7px;font-size:12.5px;line-height:19px;color:#222}
.info2 a{color:var(--blue-text);font-weight:700;text-decoration:underline;margin-left:6px}
.footer{left:0;top:1067px;width:1067px;height:97px;background:var(--dark);color:#9c9c9c;font-size:11px;line-height:16px}
.footer .col{position:absolute;top:13px;white-space:nowrap}
.footer b{color:#aaa}
.badges{position:absolute;left:488px;top:30px;display:flex;gap:10px;align-items:center}
.badge{background:#d6d6d6;border-radius:3px}
.foot-brand{position:absolute;left:822px;top:14px;width:72px;height:64px;border:2px solid #777;border-radius:4px;display:flex;align-items:center;justify-content:center;font-family:"Signika",sans-serif;font-weight:600;font-size:13px;color:#888}
.copyright{left:0;top:1164px;width:1067px;height:36px;background:var(--darker);color:#7d7d7d;font-size:11px;text-align:center;line-height:36px}
</style>
</head>
<body>
<div class="abs top-band"></div>

<header class="abs header">
  <div class="abs brand"><span class="brand-mark"></span><span class="brand-name">Brantow</span></div>
  <div class="abs social"><span class="label">Social Media:</span><span class="social-box first" aria-hidden="true"></span><span class="social-box second" aria-hidden="true"></span></div>
</header>

<nav class="abs nav">
  <a href="#" style="width:85px">Home</a>
  <a href="#" style="width:90px">Auctions</a>
  <a href="#" style="width:153px">Real Estate Listings</a>
  <a href="#" style="width:111px">Our Services</a>
  <a href="#" style="width:117px">Why Auctions</a>
  <a href="#" style="width:80px">About Us</a>
  <a href="#" style="width:107px">Past Auctions</a>
  <a href="#">Contact Us</a>
</nav>

<div class="abs hero-frame"><div class="abs hero-photo" role="img" aria-label="Stock photo of a beige suburban house with a white garage door"></div></div>

<div class="abs dropdown">
  <a href="#">Land &amp; Recreation (5)</a>
  <a class="current" href="#">Commercial (6)</a>
  <a href="#">Residential (7)</a>
  <a href="#">Homes with Acreage (8)</a>
  <a href="#" style="border-bottom:none">Oil &amp; Gas (9</a>
</div>

<section class="abs signup">
  <h2>EMAIL SIGN-UP</h2>
  <label style="top:66px">Your Name</label>
  <div class="field" style="top:90px"></div>
  <label style="top:134px;left:31px">Email Address</label>
  <div class="field" style="top:161px;left:31px"></div>
  <div class="btn">Subscribe</div>
</section>

<div class="abs content-bg"></div>

<div class="abs video" role="img" aria-label="Featured video still of an agent standing in front of a house"></div>
<div class="abs play"><svg width="36" height="36" viewBox="0 0 36 36"><path d="M14 10 L26 18 L14 26 Z" fill="#eee"/></svg></div>
<div class="abs video-bar">
  <svg class="abs" style="left:9px;top:5px" width="10" height="10"><path d="M1 1 L9 5 L1 9Z" fill="#eee"/></svg>
  <div class="track"></div><div class="fill"></div>
  <svg class="abs" style="left:191px;top:5px" width="12" height="10"><path d="M1 3h3l4-3v10l-4-3H1z" fill="#eee"/></svg>
  <svg class="abs" style="left:210px;top:5px" width="11" height="10"><rect x="1" y="1" width="9" height="8" fill="none" stroke="#eee" stroke-width="1.5"/></svg>
</div>

<section class="abs widget testimonial">
  <div class="widget-head">CLIENTS TESTIMONIALS</div>
  <span class="qmark" style="left:10px;top:36px">&ldquo;</span>
  <p class="quote">Lorem Ipsum is simply dummy text of the printing and typesetting industry. Lorem Lorem Ipsum is simply dummy text of the printing and typesetting industry. Lorem Lorem</p>
  <span class="qmark" style="left:222px;top:118px">&rdquo;</span>
  <span class="author">Elisabeth</span>
  <span class="more" style="left:156px;top:155px">read more</span>
</section>

<section class="abs widget news">
  <div class="widget-head">NEWS &amp; EVENTS</div>
  <ul>
    <li>Great Land Auction Companies Make All the Difference Great Land Auction</li>
    <li>All the Difference Great Land Auction</li>
  </ul>
  <span class="more" style="left:153px;top:150px">read more</span>
</section>

<h1 class="abs main-title">MARTIN BRANTOW AUCTIONEER REAL ESTATE BROKER</h1>
<div class="abs intro">
  <p>Buying or selling you can count on <strong class="name">Martin Brantow Auctioneer</strong> to deliver a quality auction experience. We handle all the details from initial handshake to final payment.<br>We are with you every step of the way giving our sellers the service and results they deserve.</p>
  <p class="tight">You only have one chance for a successful auction. Contact us today to see how our experience and know-how can work for you.</p>
  <p><strong>We are confident that you will appreciate our higher standard of service</strong></p>
</div>

<h2 class="abs upcoming">UPCOMING AUCTIONS</h2>
<section class="abs auction">
  <div class="auction-head">HORSES LAND NOBLE EDMONTON, ALBERTA</div>
  <div class="box thumb-box"><div class="thumb" role="img" aria-label="House photo with a for sale sign"><div class="sale-tag"></div></div></div>
  <div class="box links-box">
    <div class="links-head">LINKS</div>
    <div class="link"><svg width="18" height="10"><rect x="0" y="1" width="7" height="7" fill="#222"/><rect x="9" y="1" width="9" height="1.6" fill="#222"/><rect x="9" y="4" width="9" height="1.6" fill="#222"/><rect x="9" y="7" width="9" height="1.6" fill="#222"/></svg>Details</div>
    <div class="link"><svg width="18" height="16"><rect x="1" y="1" width="11" height="10" fill="none" stroke="#222" stroke-width="1.5"/><rect x="6" y="5" width="11" height="10" fill="#222"/></svg>Photos</div>
  </div>
  <div class="box info1">
    BILLINGS AREA * CROP &amp; TIMBER<br>
    <span class="hl">160± ACRES LAND NOBLE COUNTY</span>, <b>OK ~ BILLINGS AREA * CROP &amp; TIMBER ~ EXCELLENT HUNTING</b><br>
    ABSOLUTE AUCTION<br>
    SELLER: THE REDFIELD FOUNDATION OF OKLAHOMA
  </div>
  <div class="box info2">
    <b>LIVE ON-SITE AUCTION WITH ONLINE BIDDING</b><br>
    Begins:&nbsp; Tuesday, March 12, 2013 at 10:00 AM CDT<br>
    <a href="#">Click Here to Bid Online Now!</a><br>
    <b>Location:</b>&nbsp; See Directions<br>
    United States Billings, OK 74630
  </div>
</section>

<footer class="abs footer">
  <div class="col" style="left:112px"><b>Contact info:</b><br>Contacts: Martin Brantow<br>Phone: (270) 555-0148<br>Email: martinbrantow@mailvex.example</div>
  <div class="col" style="left:320px"><b>Address:</b><br>482 Wexcombe Lane<br>Bowling Green,<br>KY 42190</div>
  <div class="badges">
    <span class="badge" style="width:52px;height:32px;border-radius:50%"></span>
    <span class="badge" style="width:28px;height:32px"></span>
    <span class="badge" style="width:54px;height:24px"></span>
    <span class="badge" style="width:42px;height:24px"></span>
    <span class="badge" style="width:24px;height:28px"></span>
  </div>
  <div class="foot-brand">Brantow</div>
</footer>
<div class="abs copyright">Copyright (C) Martin Brantow Auctioneer Real Estate Broker Auction 2013 - 2014 .&nbsp; All Rights Reserved</div>
</body>
</html>
```